Crestline Slate & Tile Needs a Business Card

Attached you will find your logo, my photo and design guidelines for a new business card. The final design will need two separate files to create an embossed card. The cards will be printed by www.plinkprint.com (Instructions below)
Format is the Zib SQUARE card
Crestline Slate And Tile is a brick and mortar, retail stone and tile shop.
One the front:
Crestline Slate And Tile
Gerald Finchcombe
Owner
48207 Vesper Hollow Blvd
Suite R & T
Charlotte, NC 28953
Cell: 704-555-0183
Web: www.CrestlineSlateAndTile.com
(Make each word of the domain a different or alternating color)
On the back;
Something that shows beautiful colorful tile
Follow the design guide closely please. For more information see this page that describes creating the spot gloss file: https://www.plinkprint.com/us/business-cards/design-guidelines-spot-gloss
The logo is what we would like to have raised spot glossed.
Format is the Zib SQUARE card. See attahced guidlines.

```html
<!DOCTYPE html>
<html lang="en">
<head>
<meta charset="utf-8">
<title>Crestline Slate &amp; Tile – Square Business Card</title>
<link href="https://fonts.googleapis.com/css2?family=Montserrat:wght@700&family=Open+Sans:wght@400;600&display=swap" rel="stylesheet">
<style>
  :root {
    --backdrop: #b4b4b4;
    --card-paper: #ffffff;
    --card-edge: #c0682a;
    --ink-dark: #1f2a33;
    --ink-body: #222222;
    --gold: #b8893a;
    --accent-red: #b0473a;
    --photo-dark: #2e3236;
    --photo-mid: #4a4c52;
    --photo-warm: #a8755e;
  }
  * { box-sizing: border-box; margin: 0; padding: 0; }
  html, body { width: 1200px; height: 815px; overflow: hidden; }
  body {
    background: linear-gradient(180deg, #c8c8c8 0%, var(--backdrop) 100%);
    font-family: "Open Sans", Arial, sans-serif;
    color: var(--ink-body);
    position: relative;
  }
  .card {
    position: absolute;
    top: 168px;
    width: 460px;
    height: 460px;
    border: 8px solid var(--card-edge);
    background: var(--card-paper);
  }
  .card--front { left: 110px; }
  .card--back { left: 630px; }

  .card-front__inner {
    height: 100%;
    display: flex;
    flex-direction: column;
    align-items: center;
    padding-top: 52px;
    text-align: center;
  }
  .brand {
    display: flex;
    align-items: center;
    gap: 12px;
    font-weight: 600;
    font-size: 24px;
    letter-spacing: 0.06em;
    color: var(--ink-dark);
  }
  .brand__mark {
    width: 18px;
    height: 18px;
    background: var(--card-edge);
  }
  .owner-name {
    margin-top: 40px;
    font-family: "Montserrat", Arial, sans-serif;
    font-weight: 700;
    font-size: 27px;
    color: var(--ink-dark);
    letter-spacing: 0.01em;
  }
  .owner-title {
    margin-top: 2px;
    font-size: 13px;
    letter-spacing: 0.04em;
    color: var(--ink-dark);
  }
  .title-rule {
    width: 22px;
    height: 2px;
    background: var(--accent-red);
    margin-top: 7px;
  }
  .icon-row {
    display: flex;
    align-items: center;
    gap: 6px;
    margin-top: 14px;
  }
  .icon-row__line {
    width: 90px;
    height: 1px;
    background: var(--gold);
  }
  .icon { width: 20px; height: 20px; display: block; }
  .contact, .address {
    margin-top: 8px;
    font-size: 15px;
    line-height: 1.3;
  }
  .address { margin-top: 6px; }
  .web__word--dark { color: var(--ink-dark); }
  .web__word--warm { color: var(--card-edge); }
  .photo {
    width: 100%;
    height: 100%;
    background: radial-gradient(ellipse at 55% 45%, var(--photo-warm) 0%, var(--photo-mid) 45%, var(--photo-dark) 100%);
  }
</style>
</head>
<body>

<section class="card card--front">
  <div class="card-front__inner">
    <div class="brand">
      <span class="brand__mark"></span>
      <span class="brand__name">Crestline Slate &amp; Tile</span>
    </div>

    <h1 class="owner-name">GERALD FINCHCOMBE</h1>
    <p class="owner-title">OWNER</p>
    <div class="title-rule"></div>

    <div class="icon-row">
      <span class="icon-row__line"></span>
      <svg class="icon" viewBox="0 0 20 20" aria-hidden="true">
        <circle cx="10" cy="10" r="10" fill="var(--gold)"/>
        <path d="M6.5 5.5l2 0.3 0.8 2.2-1.2 0.9a6 6 0 0 0 3 3l0.9-1.2 2.2 0.8 0.3 2c-4 1-9-4-8-8z" fill="#fff"/>
      </svg>
      <svg class="icon" viewBox="0 0 20 20" aria-hidden="true">
        <circle cx="10" cy="10" r="10" fill="var(--gold)"/>
        <rect x="5" y="6.5" width="10" height="7" fill="#fff"/>
        <path d="M5 6.5l5 4 5-4" stroke="var(--gold)" stroke-width="1" fill="none"/>
      </svg>
      <svg class="icon" viewBox="0 0 20 20" aria-hidden="true">
        <circle cx="10" cy="10" r="10" fill="var(--gold)"/>
        <circle cx="10" cy="10" r="5" fill="none" stroke="#fff" stroke-width="1.2"/>
        <ellipse cx="10" cy="10" rx="2" ry="5" fill="none" stroke="#fff" stroke-width="1"/>
        <line x1="5" y1="10" x2="15" y2="10" stroke="#fff" stroke-width="1"/>
      </svg>
      <span class="icon-row__line"></span>
    </div>

    <p class="contact">
      704-555-0183<br>
      dara.whitlow@brevanto.com<br>
      <span class="web">www.<span class="web__word--dark">Crestline</span><span class="web__word--warm">Slate</span><span class="web__word--dark">And</span><span class="web__word--warm">Tile</span>.com</span>
    </p>

    <div class="icon-row">
      <span class="icon-row__line"></span>
      <svg class="icon" viewBox="0 0 20 20" aria-hidden="true">
        <circle cx="10" cy="10" r="10" fill="var(--gold)"/>
        <path d="M10 4.5a3.5 3.5 0 0 1 3.5 3.5c0 2.6-3.5 7-3.5 7s-3.5-4.4-3.5-7A3.5 3.5 0 0 1 10 4.5z" fill="#fff"/>
        <circle cx="10" cy="8" r="1.3" fill="var(--gold)"/>
      </svg>
      <span class="icon-row__line"></span>
    </div>

    <p class="address">
      48207 Vesper Hollow Blvd<br>
      Suite R &amp; T Charlotte, NC 28953
    </p>
  </div>
</section>

<section class="card card--back">
  <div class="photo" role="img" aria-label="Portrait photograph of the owner in a checked blazer and white shirt against a dark backdrop"></div>
</section>

</body>
</html>
```